Pool Screen Enclosure Building a Career Boot Camp!

Looking to Host a Boot Camp for people looking for a career or looking to change careers. We Design, Manufacture and Install Custom Pool Screen Enclosures. We have a training program to allow Non Experienced motivated people the chance at a great career that will provide a great living for them and their family. This will be a paid boot camp, week long, we provide all the initial training for them to make a transition into our business. This will be 5 days of training with a guaranteed job to start the following Monday.... This is good for both someone with no construction experience or someone with construction experience that wants to upgrade their current job.
Paid Boot Camp
transition to a full time job with great pay
Benefits include Health Insurance, Dental and Vision, 401K, we provide the tools and training.

```html
<!DOCTYPE html>
<html lang="en">
<head>
<meta charset="utf-8">
<title>Paid Boot Camp – Harbor Screen Works</title>
<link rel="stylesheet" href="https://fonts.googleapis.com/css2?family=Montserrat:wght@500;600;700;800;900&display=swap">
<style>
  :root{
    --yellow:#f6b916;
    --green:#6cbd45;
    --green-deep:#4fa33a;
    --black:#0d0d0d;
    --ink:#1a1a1a;
    --white:#ffffff;
    --hero-dark:#3a3c3e;
    --hero-mid:#5c5f61;
  }
  html,body{margin:0;padding:0;overflow:hidden;background:#f2f2f0;}
  .flyer{
    position:relative;width:950px;height:1200px;overflow:hidden;
    background:var(--white);font-family:"Montserrat",sans-serif;color:var(--ink);
  }
  .backdrop{position:absolute;inset:0;}
  .brand{
    position:absolute;left:40px;top:92px;display:flex;align-items:center;gap:14px;
  }
  .brand-dot{width:44px;height:44px;border-radius:50%;background:var(--green);}
  .brand-name{font-weight:700;font-size:34px;color:var(--green);letter-spacing:-0.5px;}
  .headline{
    position:absolute;left:0;right:0;top:370px;text-align:center;text-transform:uppercase;
  }
  .headline h1{
    margin:0 0 0 30px;font-weight:900;font-size:64px;line-height:1;color:var(--yellow);
    -webkit-text-stroke:2px var(--black);paint-order:stroke fill;
    text-shadow:0 3px 6px rgba(0,0,0,.6);
  }
  .headline p{
    margin:10px 0 0 30px;font-weight:800;font-size:36px;line-height:1.1;color:var(--green);
    -webkit-text-stroke:1.5px var(--black);paint-order:stroke fill;
    text-shadow:0 2px 5px rgba(0,0,0,.6);
  }
  .intro{
    position:absolute;left:32px;top:770px;width:545px;font-size:16.6px;line-height:1.45;font-weight:500;
  }
  .intro p{margin:0 0 24px;}
  .intro .hl{color:var(--green);font-weight:600;}
  .benefits{
    position:absolute;left:648px;top:704px;width:290px;font-weight:700;color:var(--ink);
  }
  .benefits h2{margin:0 0 18px;font-size:20px;text-decoration:underline;text-underline-offset:3px;font-weight:800;}
  .benefits ul{margin:0;padding:0 0 0 24px;list-style:none;}
  .benefits li{font-size:20.5px;line-height:1.2;margin-bottom:20px;padding-left:14px;text-indent:-14px;}
  .benefits li::before{content:"•";margin-right:6px;}
  .contact{
    position:absolute;left:642px;top:955px;width:282px;background:var(--white);
    box-shadow:0 4px 10px rgba(0,0,0,.2);text-align:center;
  }
  .contact-head{
    background:var(--black);height:64px;display:flex;align-items:center;justify-content:center;gap:8px;
  }
  .contact-head .brand-dot{width:22px;height:22px;}
  .contact-head .brand-name{font-size:17px;}
  .contact-body{padding:18px 10px 20px;}
  .address{font-size:13.5px;font-weight:700;line-height:1.3;margin:0;}
  .phone{font-size:29px;font-weight:700;color:var(--green);margin:8px 0 6px;}
  .email{font-size:14.5px;font-weight:700;margin:0;}
  .base-band{position:absolute;left:0;right:0;bottom:0;height:18px;}
  .base-band .y{height:8px;background:var(--yellow);}
  .base-band .g{height:10px;background:var(--green);}
</style>
</head>
<body>
<div class="flyer">
  <svg class="backdrop" width="950" height="1200" viewBox="0 0 950 1200">
    <defs>
      <linearGradient id="heroTone" x1="0" y1="0" x2="0" y2="1">
        <stop offset="0" stop-color="#4b4e51"/>
        <stop offset=".55" stop-color="#5d6063"/>
        <stop offset="1" stop-color="#2f3a38"/>
      </linearGradient>
      <radialGradient id="crewTone" cx=".5" cy=".45" r=".6">
        <stop offset="0" stop-color="#c9c2b4"/><stop offset="1" stop-color="#8c8576"/>
      </radialGradient>
      <radialGradient id="roofTone" cx=".5" cy=".4" r=".6">
        <stop offset="0" stop-color="#b7c9dc"/><stop offset="1" stop-color="#6a7b8d"/>
      </radialGradient>
      <radialGradient id="frameTone" cx=".5" cy=".4" r=".6">
        <stop offset="0" stop-color="#d3d6d8"/><stop offset="1" stop-color="#8d8f8c"/>
      </radialGradient>
    </defs>
    <rect x="0" y="0" width="950" height="690" fill="url(#heroTone)" role="img" aria-label="Photo of a finished pool screen enclosure at dusk beside a lake"/>
    <path d="M0 0H665C575 130 380 210 0 262Z" fill="var(--black)"/>
    <path d="M610 0H672C590 140 400 210 150 226C370 200 545 120 610 0Z" fill="var(--yellow)"/>
    <path d="M0 612C160 575 360 590 520 650C620 688 700 700 800 690L950 690V1200H0Z" fill="var(--white)"/>
    <path d="M520 650C660 710 860 690 950 500V610C880 700 700 720 540 670Z" fill="var(--green)"/>
    <path d="M540 670C700 720 880 700 950 600V965H614V695C590 688 565 680 540 670Z" fill="var(--yellow)"/>
    <g stroke="#ffffff" stroke-width="4">
      <circle cx="115" cy="653" r="80" fill="url(#crewTone)" role="img" aria-label="Photo of trainees studying enclosure plans on site"/>
      <circle cx="303" cy="653" r="80" fill="url(#roofTone)" role="img" aria-label="Photo of installers fitting a roof panel"/>
      <circle cx="492" cy="653" r="80" fill="url(#frameTone)" role="img" aria-label="Photo of a worker on a ladder assembling an enclosure frame"/>
    </g>
  </svg>

  <div class="brand">
    <span class="brand-dot"></span>
    <span class="brand-name">Harbor Screen Works</span>
  </div>

  <div class="headline">
    <h1>Paid Boot Camp</h1>
    <p>Transition to a full time<br>job with great pay</p>
  </div>

  <div class="intro">
    <p>Looking to Host a Boot Camp for people looking for a career or looking to change careers. We <span class="hl">Design, Manufacture</span> and <span class="hl">Install Custom Pool Screen Enclosures</span>. We have a <span class="hl">training program</span> to allow <span class="hl">Non Experienced motivated people</span> the chance at a great career that will provide a great living for them and their family.</p>
    <p>This will be a <span class="hl">PAID BOOT CAMP</span>, week long, we provide all the initial training for them to make a transition into our business. This will be <span class="hl">5 DAYS</span> of training with a <span class="hl">GUARANTEED JOB</span> to start the following Monday....</p>
    <p>This is good for both someone with no <span class="hl">CONSTRUCTION EXPERIENCE</span> or someone with construction experience that wants to upgrade their current job.</p>
  </div>

  <div class="benefits">
    <h2>BENEFITS INCLUDE:</h2>
    <ul>
      <li>Health Insurance</li>
      <li>Dental and Vision</li>
      <li>401K</li>
      <li>we provide the tools and training</li>
    </ul>
  </div>

  <div class="contact">
    <div class="contact-head">
      <span class="brand-dot"></span>
      <span class="brand-name">Harbor Screen Works</span>
    </div>
    <div class="contact-body">
      <p class="address">412 W PALMETTO AVENUE,<br>PORT LUCIE FL 34900</p>
      <p class="phone">555-014-2290</p>
      <p class="email">hello@harborscreenworks.com</p>
    </div>
  </div>

  <div class="base-band"><div class="y"></div><div class="g"></div></div>
</div>
</body>
</html>
```